Brochure for new townhouse development

We need a brochure created for our new townhouse development that we can provide to potential purchasers for off-the-plan sales.

2 similar examples are attached.

Brochure content is to include the text as per the attached word document (brochure text) and as follows:
Cover
The Development
At a Glance
The Location - also to include the 2d map and aerial photo (have included screenshot of map and aerial photo as a placeholder, to be replaced in the final version)
Plans - include 3d floor plans, I have included a sample 3d floor plan as a placeholder, this is to be replaced in the final version.
Finishes - as per word document attached, and colour samples attached
Specifications - as per word document attached
Subdivision plan - I have attached a plan which can be used as a placeholder, the final version will be ready next week and is to be replaced in the final version
Landscape plan - as per attached
Rental assessment - as per attached
Stake your Claim

Renders of the building are attached and can be used throughout the brochure.

There is no company name or logo to include.

We have other upcoming developments and would look to reuse the winning brochure so there is future and ongoing work.

```html
<!DOCTYPE html>
<html lang="en">
<head>
<meta charset="utf-8">
<title>Townhouse Brochure – Page Layouts</title>
<link rel="stylesheet" href="https://fonts.googleapis.com/css2?family=Open+Sans:wght@400;600;700;800&display=swap">
<style>
  :root{
    --board:#363638;
    --page:#ffffff;
    --slate:#58585a;
    --ink:#3a3a3c;
    --night:#141416;
    --white:#ffffff;
  }
  *{margin:0;padding:0;box-sizing:border-box;}
  html,body{width:1035px;height:1200px;overflow:hidden;background:var(--board);}
  body{font-family:"Open Sans",Arial,sans-serif;position:relative;}

  .board-label{position:absolute;transform:translateX(-50%);color:var(--white);font-weight:700;font-size:25px;line-height:1;white-space:nowrap;}

  .page{position:absolute;width:424px;height:300px;background:var(--page);overflow:hidden;}
  .col-left{left:65px;}
  .col-right{left:546px;}
  .row-1{top:108px;}
  .row-2{top:464px;}
  .row-3{top:831px;}

  .photo{position:absolute;}
  .slant{position:absolute;left:0;top:0;width:424px;height:300px;}

  .section-title{position:absolute;font-weight:700;font-size:8px;line-height:1;padding-bottom:2px;border-bottom:0.6px solid currentColor;}

  /* back cover */
  .location-panel{left:0;top:30px;width:404px;height:239px;background:linear-gradient(160deg,#1e1f1f 0%,#121213 55%,#0d0d0e 100%);}
  .back .copy{position:absolute;color:var(--white);font-size:5.4px;line-height:7.2px;}
  .back .section-title{color:var(--white);}
  .back .sub-title{position:absolute;color:var(--white);font-weight:700;font-size:7.5px;}

  /* cover */
  .cover-photo{left:0;top:30px;width:404px;height:239px;background:linear-gradient(180deg,#cfdff0 0%,#e5e8ee 35%,#b48f66 55%,#7b7467 78%,#c9c9c6 100%);}
  .cover-tint{position:absolute;left:268px;top:30px;width:115px;height:270px;background:rgba(38,38,40,0.78);}
  .cover-rule{position:absolute;left:284px;top:192px;width:1px;height:77px;background:var(--white);}
  .cover-heading{position:absolute;left:290px;top:189px;color:var(--white);font-weight:700;font-size:15.5px;line-height:18px;letter-spacing:0.2px;}
  .cover-address{position:absolute;left:284px;top:279px;color:var(--white);font-weight:700;font-size:5.4px;letter-spacing:0.2px;}

  /* development page */
  .dev .section-title{color:var(--ink);}
  .dev-body{position:absolute;left:34px;top:76px;width:135px;color:var(--ink);font-size:4.3px;line-height:5.9px;text-align:justify;}
  .dev-body p{margin-bottom:4px;}
  .glance .section-title{color:var(--white);}
  .glance-list{position:absolute;left:203px;top:76px;width:190px;list-style:none;color:var(--white);font-size:5.4px;line-height:7.4px;}
  .glance-list li{position:relative;padding-left:18px;}
  .glance-list .dot::before{content:"•";position:absolute;left:0;}
  .glance-list .ring::before{content:"o";position:absolute;left:0;}
  .glance-list .gap{margin-top:7px;}

  /* tagline */
  .tagline{position:absolute;right:54px;top:243px;text-align:right;font-weight:700;font-size:8px;line-height:10px;}
  .tagline .address{display:block;margin-top:7px;font-size:5.4px;line-height:1;}
  .tagline.on-white{color:var(--ink);}
  .tagline.on-slate{color:var(--white);}

  /* gallery pages */
  .gallery-photo{left:32px;top:21px;width:361px;height:241px;}
  .exterior-photo{background:linear-gradient(180deg,#c9d8e8 0%,#e7e1d6 30%,#b18f6b 55%,#8f8f93 75%,#2e2f33 100%);}
  .kitchen-photo{background:linear-gradient(100deg,#efedea 0%,#d4b591 35%,#f2f1ee 55%,#7f8a64 80%,#c99e71 100%);}
  .living-photo{background:linear-gradient(100deg,#7d8a68 0%,#c9c9c3 30%,#f3f2ef 55%,#9a5b3c 72%,#d9b68f 100%);}
  .room-label{position:absolute;left:46px;top:276px;color:var(--ink);font-weight:600;font-size:7px;letter-spacing:0.3px;padding-bottom:2px;border-bottom:0.6px solid var(--ink);width:50px;}
</style>
</head>
<body>

  <div class="board-label" style="left:285px;top:64px;">back</div>
  <div class="board-label" style="left:768px;top:64px;">TITLE</div>
  <div class="board-label" style="left:290px;top:420px;">page-01</div>
  <div class="board-label" style="left:771px;top:417px;">page-02</div>
  <div class="board-label" style="left:290px;top:776px;">page-03</div>
  <div class="board-label" style="left:771px;top:781px;">page-04</div>

  <!-- Back cover: The Location -->
  <section class="page back col-left row-1">
    <div class="photo location-panel" role="img" aria-label="Darkened render of the townhouse exterior behind the location text"></div>
    <h2 class="section-title" style="left:70px;top:61px;">The Location</h2>
    <p class="copy" style="left:70px;top:79px;width:220px;">A location without equal, within strolling distance of Westhaven's premier boutique shopping and dining destination or a short drive to the CBD, zoned for top schools and with several private schools within easy reach.</p>

    <h3 class="sub-title" style="left:70px;top:115px;">In the vicinity:</h3>
    <p class="copy" style="left:70px;top:130px;">Larchmere Mall<br>St Aldric's Hospital<br>Birchwood Park<br>Marlow Street<br>Foxley Park</p>
    <p class="copy" style="left:141px;top:130px;">(2 min walk – 140 m)<br>(7 min walk – 550 m)<br>(12 min walk – 1 km)<br>(3 min drive – 1.5 km)<br>(3 min drive – 1.6 km)</p>

    <h3 class="sub-title" style="left:234px;top:115px;">Nearby private schools:</h3>
    <p class="copy" style="left:234px;top:130px;">Ardenne House School<br>Tarn Vale Girls' School<br>St Briony's College<br>St Colum's College</p>

    <h3 class="sub-title" style="left:70px;top:181px;">Zoned for:</h3>
    <p class="copy" style="left:70px;top:195px;">Birchwood Normal School<br>St Ewan's School<br>Hollis Normal Intermediate<br>Northbrook High School<br>Westhaven Boys' High School<br>Westhaven Girls' High School</p>

    <h3 class="sub-title" style="left:234px;top:181px;">Stake your claim</h3>
    <p class="copy" style="left:234px;top:195px;width:120px;">Act now to secure your piece of this exceptional development.<br>Speak to xxxx<br>by phone (xxx)<br>email xxx today</p>
  </section>

  <!-- Cover -->
  <section class="page cover col-right row-1">
    <div class="photo cover-photo" role="img" aria-label="Exterior render of the timber-clad gabled townhouses from the street"></div>
    <div class="cover-tint"></div>
    <div class="cover-rule"></div>
    <h1 class="cover-heading">Perfectly<br>Positioned<br>Urban<br>Living</h1>
    <p class="cover-address">24 HALDEN ROAD</p>
  </section>

  <!-- The Development / At a Glance -->
  <section class="page dev col-left row-2">
    <h2 class="section-title" style="left:34px;top:55px;">The Development</h2>
    <div class="dev-body">
      <p>24 Halden Road, Larchmere, is a brand-new development of six contemporary townhouses in an unrivalled location, poised to enjoy a vibrant urban lifestyle within easy reach of Larchmere Village and the city, and zoned for top schools.</p>
      <p>Two blocks of three residences offer stylish, hassle-free living. Each townhouse comprises two bedrooms, two en suite bathrooms, single internal-access garage and private courtyard. Smart design, premium finishes and freehold titles ensure a quality project with a premium address.</p>
      <p>On the ground floor, open-plan living and dining flows to a low-maintenance courtyard garden for outdoor living and entertaining. Connected by a breakfast bar, a sleek, chic and functional kitchen boasts high-quality appliances.</p>
      <p>Upstairs are two double bedrooms, each served by a high-spec tiled en suite bathroom. Two of the townhouses feature a walk-in robe in the master, while other bedrooms include built-in wardrobes.</p>
      <p>A downstairs guest WC and single internal-access garage with laundry add superb convenience.</p>
      <p>Architecturally designed by Marden Architecture, these homes are scheduled for completion by the end of 2021. Developments of this quality – in a location of this calibre – are all too rare, so this is the time to make your move.</p>
    </div>

    <svg class="slant glance-panel" viewBox="0 0 424 300" aria-hidden="true">
      <polygon points="188,29 424,29 424,206 188,274" fill="var(--slate)"/>
    </svg>
    <div class="glance">
      <h2 class="section-title" style="left:203px;top:55px;">At a Glance</h2>
      <ul class="glance-list">
        <li class="dot">Two blocks of three architecturally designed townhouses</li>
        <li class="dot">Each townhouse includes:</li>
        <li class="ring gap">Open-plan living, dining and high-spec kitchen</li>
        <li class="ring">Seamless flow to easy-care courtyard garden</li>
        <li class="ring">Two double bedrooms, all with built-in wardrobes<br>(two townhouses with WIR in master)</li>
        <li class="ring">Two en suite tiled bathrooms</li>
        <li class="ring">Single internal-access garage with laundry</li>
        <li class="dot gap">Smart design, high-quality fixtures and fittings,<br>and freehold titles</li>
      </ul>
    </div>

    <p class="tagline on-white">Perfectly<br>Positioned<br>Urban Living<span class="address">24 Halden Road</span></p>
  </section>

  <!-- Exterior -->
  <section class="page col-right row-2">
    <div class="photo gallery-photo exterior-photo" role="img" aria-label="Exterior render of the townhouses with garages and driveway"></div>
    <svg class="slant" viewBox="0 0 424 300" aria-hidden="true"><polygon points="118,300 424,210 424,300" fill="var(--slate)"/></svg>
    <p class="room-label">EXTERIOR</p>
    <p class="tagline on-slate">Perfectly<br>Positioned<br>Urban Living<span class="address">24 Halden Road</span></p>
  </section>

  <!-- Kitchen -->
  <section class="page col-left row-3">
    <div class="photo gallery-photo kitchen-photo" role="img" aria-label="Interior render of the kitchen and dining area opening to the garden"></div>
    <svg class="slant" viewBox="0 0 424 300" aria-hidden="true"><polygon points="118,300 424,210 424,300" fill="var(--slate)"/></svg>
    <p class="room-label">KITCHEN</p>
    <p class="tagline on-slate">Perfectly<br>Positioned<br>Urban Living<span class="address">24 Halden Road</span></p>
  </section>

  <!-- Living space -->
  <section class="page col-right row-3">
    <div class="photo gallery-photo living-photo" role="img" aria-label="Interior render of the living room with sofa and courtyard doors"></div>
    <svg class="slant" viewBox="0 0 424 300" aria-hidden="true"><polygon points="118,300 424,210 424,300" fill="var(--slate)"/></svg>
    <p class="room-label" style="width:80px;">LIVING SPACE</p>
    <p class="tagline on-slate">Perfectly<br>Positioned<br>Urban Living<span class="address">24 Halden Road</span></p>
  </section>

</body>
</html>
```